MALT HIGHLANDS/STONEFERN DISTILLERY

DOUBLE SIDED BUSINESS CARD ONE SIDE FOR WWW.MALTHIGHLANDS-EXAMPLE.ORG AND ONE SIDE FOR STONEFERN DISTILLERY ARTWORK FOR WEBSITE IS ATTACHED

1)
GORDON PRYCE CEO
MALT HIGHLANDS
Office 1 Harbour Court
14 Ferrier Row
Glasgow
Scotland, G5 2KX
W:WWW.MALTHIGHLANDS-EXAMPLE.ORG
E:GORDON@MALTHIGHLANDS-EXAMPLE.ORG
T:+44 7491 305718

2)
GORDON PRYCE CEO
STONEFERN DISTILLERY
Building 148, Werfpark Zandhoven,
3e Brederolaan, Katwijk, 2219KP

W: WWW.stonefern-example.nl
E: GORDON@stonefern-example.nl
T:+44 7491 305718

1)
Marieke Dool DIRECTOR
MALT HIGHLANDS
Office 1 Harbour Court
14 Ferrier Row
Glasgow
Scotland, G5 2KX
W:WWW.MALTHIGHLANDS-EXAMPLE.ORG
E:Marieke@MALTHIGHLANDS-EXAMPLE.ORG
T:+31 6 58137704

2)
MARIEKE DOOL DIRECTOR
STONEFERN DISTILLERY

E: marieke@stonefern-example.nl
T:+31 6 58137704

```html
<!DOCTYPE html>
<html lang="en">
<head>
<meta charset="utf-8">
<title>Malt Highlands / Stonefern Distillery business cards</title>
<link rel="stylesheet" href="https://fonts.googleapis.com/css2?family=Cormorant+Garamond:wght@500&family=Montserrat:wght@400;500;600&display=swap">
<style>
  :root {
    --bg: #ececec;
    --paper: #ffffff;
    --ink: #1f1f1f;
    --card-dark: #141414;
    --gold: #c9a03a;
    --gold-soft: #f4efe3;
    --band-grey: #5a5a5a;
    --text: #2a2a2a;
  }
  * { margin: 0; padding: 0; box-sizing: border-box; }
  html, body { width: 1200px; height: 900px; overflow: hidden; background: var(--bg); }
  body { position: relative; font-family: "Montserrat", sans-serif; color: var(--text); }

  .card { position: absolute; overflow: hidden; }
  .card--light { background: var(--paper); }
  .card--dark { background: var(--card-dark); display: flex; align-items: center; justify-content: center; }

  .card--malt-front { left: 136px; top: 124px; width: 434px; height: 260px; }
  .card--malt-back { left: 634px; top: 124px; width: 438px; height: 263px; }
  .card--stone-front { left: 136px; top: 498px; width: 439px; height: 264px; }
  .card--stone-back { left: 634px; top: 498px; width: 444px; height: 265px; }

  .backdrop-mark {
    position: absolute; border-radius: 50%;
    background: radial-gradient(circle, var(--gold-soft) 0%, rgba(244,239,227,0) 70%);
  }
  .card--malt-front .backdrop-mark { left: 230px; top: -20px; width: 220px; height: 220px; }
  .card--stone-front .backdrop-mark { left: 300px; top: -10px; width: 190px; height: 190px; }

  /* brand lockups */
  .brand { position: absolute; display: flex; flex-direction: column; align-items: center; }
  .brand__dot { width: 14px; height: 14px; border-radius: 50%; background: var(--gold); margin-bottom: 10px; }
  .brand__name--malt {
    font-family: "Cormorant Garamond", serif; font-weight: 500; color: var(--gold);
    font-size: 30px; line-height: 1; letter-spacing: 2px; text-align: center;
  }
  .card--malt-front .brand { left: 22px; top: 44px; width: 166px; }
  .card--malt-back .brand { position: static; }
  .card--malt-back .brand__dot { width: 20px; height: 20px; margin-bottom: 16px; }
  .card--malt-back .brand__name--malt { font-size: 46px; }

  .brand--stone { flex-direction: row; align-items: center; gap: 10px; }
  .brand__square { width: 14px; height: 14px; background: var(--gold); }
  .brand__name--stone {
    font-family: "Montserrat", sans-serif; font-weight: 600; color: var(--ink);
    font-size: 20px; line-height: 1.1; letter-spacing: 1px;
  }
  .card--stone-front .brand { left: 30px; top: 50px; }
  .card--stone-back .brand { position: static; }
  .card--stone-back .brand__square { width: 22px; height: 22px; }
  .card--stone-back .brand__name--stone { color: #ffffff; font-size: 30px; }

  /* person */
  .person { position: absolute; text-align: right; }
  .card--malt-front .person { right: 22px; top: 154px; }
  .card--stone-front .person { right: 21px; top: 158px; }
  .person__name--serif { font-family: "Cormorant Garamond", serif; font-weight: 500; font-size: 22px; color: var(--gold); line-height: 1; }
  .person__name--sans { font-family: "Montserrat", sans-serif; font-weight: 500; font-size: 15px; color: var(--gold); line-height: 1; letter-spacing: -0.2px; }
  .person__role { font-size: 10.5px; margin-top: 8px; }

  .rule { position: absolute; height: 1px; background: var(--gold); }
  .card--malt-front .rule { left: 30px; top: 196px; width: 382px; }
  .card--stone-front .rule { left: 24px; top: 198px; width: 392px; }

  .contacts { position: absolute; list-style: none; font-size: 10px; line-height: 13.5px; }
  .contacts li { display: flex; align-items: center; gap: 6px; }
  .contacts svg { width: 9px; height: 9px; fill: var(--gold); flex: none; }
  .card--malt-front .contacts { left: 29px; top: 203px; }
  .card--stone-front .contacts { left: 24px; top: 205px; }

  .address { position: absolute; text-align: right; font-size: 10px; line-height: 12.5px; font-style: normal; }
  .card--malt-front .address { right: 22px; top: 206px; }
  .card--stone-front .address { right: 17px; top: 216px; }

  .band { position: absolute; left: 0; right: 0; bottom: 0; height: 8px; }
  .band__gold { position: absolute; left: 0; top: 0; height: 100%; background: var(--gold); }
  .band__grey { position: absolute; top: 0; right: 0; height: 100%; background: var(--band-grey); }
  .card--malt-front .band__gold { width: 283px; clip-path: polygon(0 0, 100% 0, calc(100% - 8px) 100%, 0 100%); }
  .card--malt-front .band__grey { width: 148px; clip-path: polygon(8px 0, 100% 0, 100% 100%, 0 100%); }
  .card--stone-front .band__gold { width: 288px; clip-path: polygon(0 0, 100% 0, calc(100% - 8px) 100%, 0 100%); }
  .card--stone-front .band__grey { width: 148px; clip-path: polygon(8px 0, 100% 0, 100% 100%, 0 100%); }
</style>
</head>
<body>
<svg width="0" height="0" style="position:absolute">
  <defs>
    <symbol id="icon-phone" viewBox="0 0 10 10"><path d="M1 3.2C1 2 2.6 1 5 1s4 1 4 2.2V4H6.8V3.2H3.2V4H1zM2 5h6l1 4H1z"/></symbol>
    <symbol id="icon-mail" viewBox="0 0 10 10"><path d="M0 2h10v1L5 6 0 3zM0 4l5 3 5-3v4H0z"/></symbol>
    <symbol id="icon-globe" viewBox="0 0 10 10"><path d="M5 0a5 5 0 1 0 0 10A5 5 0 0 0 5 0zm0 1.2c.5.6.9 1.6 1 2.8H4c.1-1.2.5-2.2 1-2.8zM4 6h2c-.1 1.2-.5 2.2-1 2.8-.5-.6-.9-1.6-1-2.8zM1.3 4h1.6a7 7 0 0 1 .5-2.5A3.8 3.8 0 0 0 1.3 4zm0 2a3.8 3.8 0 0 0 2.1 2.5A7 7 0 0 1 2.9 6zm5.8 0a7 7 0 0 1-.5 2.5A3.8 3.8 0 0 0 8.7 6zm1.6-2a3.8 3.8 0 0 0-2.1-2.5c.3.7.5 1.6.5 2.5z"/></symbol>
  </defs>
</svg>

<section class="card card--light card--malt-front" aria-label="Malt Highlands card front">
  <div class="backdrop-mark" role="img" aria-label="Faint brand emblem backdrop"></div>
  <div class="brand">
    <span class="brand__dot"></span>
    <span class="brand__name--malt">MALT<br>HIGHLANDS</span>
  </div>
  <div class="person">
    <p class="person__name--serif">Marieke Dool</p>
    <p class="person__role">Director</p>
  </div>
  <div class="rule"></div>
  <ul class="contacts">
    <li><svg><use href="#icon-phone"/></svg>+31 6 58137704</li>
    <li><svg><use href="#icon-mail"/></svg>Marieke@malthighlands-example.org</li>
    <li><svg><use href="#icon-globe"/></svg>www.malthighlands-example.org</li>
  </ul>
  <address class="address">Office 1 Harbour Court<br>14 Ferrier Row<br>Glasgow, Scotland, G5 2KX</address>
  <div class="band"><span class="band__gold"></span><span class="band__grey"></span></div>
</section>

<section class="card card--dark card--malt-back" aria-label="Malt Highlands card back">
  <div class="brand">
    <span class="brand__dot"></span>
    <span class="brand__name--malt">MALT<br>HIGHLANDS</span>
  </div>
</section>

<section class="card card--light card--stone-front" aria-label="Stonefern Distillery card front">
  <div class="backdrop-mark" role="img" aria-label="Faint brand emblem backdrop"></div>
  <div class="brand brand--stone">
    <span class="brand__square"></span>
    <span class="brand__name--stone">STONEFERN<br>DISTILLERY</span>
  </div>
  <div class="person">
    <p class="person__name--sans">MARIEKE DOOL</p>
    <p class="person__role">Director</p>
  </div>
  <div class="rule"></div>
  <ul class="contacts">
    <li><svg><use href="#icon-phone"/></svg>+31 6 58137704</li>
    <li><svg><use href="#icon-mail"/></svg>marieke@stonefern-example.nl</li>
    <li><svg><use href="#icon-globe"/></svg>www.stonefern-example.nl</li>
  </ul>
  <address class="address">Building 148, Werfpark Zandhoven<br>3e Brederolaan, Katwijk, 2219KP</address>
  <div class="band"><span class="band__gold"></span><span class="band__grey"></span></div>
</section>

<section class="card card--dark card--stone-back" aria-label="Stonefern Distillery card back">
  <div class="brand brand--stone">
    <span class="brand__square"></span>
    <span class="brand__name--stone">STONEFERN<br>DISTILLERY</span>
  </div>
</section>
</body>
</html>
```